Health care technology software systems

We have a solid logo. We have company colors that will need to be used as well. We just need a great business card design. We sell to health plans but want to be modern
Updates

Need extra days to review

Target Market(s)

Health technology sector selling into Health Plans

Industry/Entity Type

Health Care Technology

Contact Information for Business Card

Name, title, address, phone number, email

Requirements
Must have
• Use of Kembrata corporate colors - Uploaded w/ our logos

```html
<!DOCTYPE html>
<html lang="en">
<head>
<meta charset="utf-8">
<title>Kembrata business card</title>
<link rel="stylesheet" href="https://fonts.googleapis.com/css2?family=Open+Sans:wght@300;400;700&display=swap">
<style>
  :root {
    --backdrop: #ececec;
    --paper: #f7f7f7;
    --charcoal: #414340;
    --ink: #3a3b3d;
    --brand-blue: #2a9fd8;
    --brand-green: #8ab833;
    --brand-navy: #4a5fa8;
    --rule: #c9c9c9;
    --wordmark-light: #e9e9e9;
  }
  * { box-sizing: border-box; margin: 0; padding: 0; }
  html, body {
    width: 1200px; height: 1126px; overflow: hidden;
    background: var(--backdrop);
    font-family: "Open Sans", Arial, sans-serif;
  }
  .sheet {
    width: 1200px; height: 1126px;
    display: flex; flex-direction: column;
    align-items: center; justify-content: center; gap: 80px;
  }
  .card {
    width: 700px; height: 400px;
    box-shadow: 0 6px 18px rgba(0,0,0,0.12);
    position: relative;
    display: flex; align-items: center;
  }
  .card--back {
    background: var(--charcoal);
    justify-content: center;
  }
  .card--front {
    background: var(--paper);
  }
  .brand {
    display: flex; align-items: center; gap: 16px;
  }
  .brand__dot {
    width: 38px; height: 38px; border-radius: 50%;
    background: var(--brand-blue);
  }
  .brand__name {
    font-weight: 300; letter-spacing: 1px;
    color: var(--ink);
  }
  .card--back .brand__name { color: var(--wordmark-light); font-size: 66px; }
  .card--back .brand__dot { width: 48px; height: 48px; }
  .card--front .brand__name { font-size: 44px; }
  .front__brand-side {
    width: 340px; height: 100%;
    display: flex; align-items: center; justify-content: center;
  }
  .front__divider {
    width: 1px; height: 170px; background: var(--rule);
  }
  .contact {
    padding-left: 34px;
    color: var(--ink);
  }
  .contact__name {
    font-size: 29px; font-weight: 700; color: var(--brand-blue); line-height: 1.1;
  }
  .contact__title {
    font-size: 15px; margin-bottom: 18px;
  }
  .contact__list { list-style: none; font-size: 15px; line-height: 1.6; }
  .contact__item { display: flex; align-items: center; gap: 9px; }
  .contact__icon { width: 14px; height: 14px; flex: none; }
  .contact__item--plain { padding-left: 0; }
</style>
</head>
<body>
<main class="sheet">
  <section class="card card--back" aria-label="Card back">
    <div class="brand">
      <span class="brand__dot"></span>
      <span class="brand__name">kembrata</span>
    </div>
  </section>

  <section class="card card--front" aria-label="Card front">
    <div class="front__brand-side">
      <div class="brand">
        <span class="brand__dot"></span>
        <span class="brand__name">kembrata</span>
      </div>
    </div>
    <div class="front__divider"></div>
    <div class="contact">
      <h1 class="contact__name">Daniel Harlow</h1>
      <p class="contact__title">Managing Director</p>
      <ul class="contact__list">
        <li class="contact__item">
          <svg class="contact__icon" viewBox="0 0 16 16"><path d="M4 1.5l2.2 3-1.3 1.6c.9 2 2.4 3.5 4.4 4.4l1.6-1.3 3 2.2-1.2 2.6C7 13.7 2.3 9 1.5 2.7z" fill="var(--brand-green)"/></svg>
          555.014.2286
        </li>
        <li class="contact__item">
          <svg class="contact__icon" viewBox="0 0 16 16" fill="none" stroke="var(--brand-blue)" stroke-width="1.3"><rect x="1.5" y="3.5" width="13" height="9"/><path d="M1.5 3.5l6.5 5 6.5-5"/></svg>
          contact@kembrata.com
        </li>
        <li class="contact__item">
          <svg class="contact__icon" viewBox="0 0 16 16" fill="none" stroke="var(--brand-navy)" stroke-width="1.2"><circle cx="8" cy="8" r="6.5"/><ellipse cx="8" cy="8" rx="3" ry="6.5"/><path d="M1.5 8h13M2.5 4.8h11M2.5 11.2h11"/></svg>
          www.kembrata.com
        </li>
        <li class="contact__item contact__item--plain">Linden Falls, Oregon, United States</li>
      </ul>
    </div>
  </section>
</main>
</body>
</html>
```